Project Management - Web Design Project

Vantrel 4 Management Limited is a company which provides specialist Project Control and Contract Management expertise to the Engineering, Construction and Manufacturing industries. The emphasis is on advanced Project Management techniques in particular Planning & Scheduling, Cost Control, Change Control, Risk Management, Reporting and Contract Administration. We are a global company (albeit a small start-up at this time) and pride ourselves on our ability to support projects to help them achieve their goals and objectives. Our aim is to implement work class control tools in a simple and user friendly manner. We would like the website to appear professional but at the same time easy to navigate and a good balance between text and pictures. The final design should communicate our value added service to our customers, our willingness to support and our structured approach to our work.

Target Market(s)

Project Management professionals working for engineering, construction and manufacturing organisations involved with delivering projects.

Industry/Entity Type

Construction

Requirements
Must have
• The website must include all of the content from the attached Excel brief. The company logo (attached) must also be included in the design. The design must portray a professional look and feel. Please include pictures and photographs related to project management in the engineering, construction and manufacturing industries. We may supplement with pictures of our own during the next steps.
Nice to have
• Emphasis that Vantrel 4 is available to support, guide, direct to achieve positive outcomes for the projects. We work hard at developing our customer relationships. Our employees are experienced in advanced project management techniques.
Should not have
• The design should not use old style fonts. It should look modern and professional. Do not include cartoons or silly illustrations.

```html
<!DOCTYPE html>
<html lang="en">
<head>
<meta charset="utf-8">
<title>Vantrel 4 Management Limited</title>
<link href="https://fonts.googleapis.com/css2?family=Arimo:wght@400;700&display=swap" rel="stylesheet">
<style>
:root{
  --page:#ffffff;
  --header:#ededed;
  --band:#e9e9e9;
  --ink:#4a4a4a;
  --muted:#8a8a8a;
  --rule:#cfcfcf;
  --blue:#1f6fd0;
  --nav-top:#9a9a9a;
  --nav-bot:#5e5e5e;
  --footer:#232323;
}
*{margin:0;padding:0;box-sizing:border-box}
html,body{width:1032px;height:1200px;overflow:hidden;background:var(--page)}
body{position:relative;font-family:"Arimo",Arial,sans-serif;color:var(--ink)}
.abs{position:absolute}
.header-band{left:0;top:0;width:1032px;height:162px;background:var(--header)}
.feature-band{left:0;top:162px;width:1032px;height:309px;background:var(--band)}
.brand{left:95px;top:10px;width:150px;height:92px;text-align:center}
.brand-mark{width:56px;height:56px;border-radius:50%;background:#2a63b8;margin:0 auto 6px}
.brand-name{font-size:15px;letter-spacing:1px;color:#5b5b5b;line-height:15px}
.brand-sub{font-size:8px;letter-spacing:1.5px}
.search{left:712px;top:20px;width:191px;height:24px;border:1px solid #9a9a9a;border-radius:4px;background:#f7f7f7;font-size:9px;color:#aaa;padding:9px 0 0 10px}
.search svg{position:absolute;right:6px;top:3px}
.nav{left:244px;top:53px;width:660px;height:42px;border-radius:3px;background:linear-gradient(var(--nav-top),var(--nav-bot));display:flex;align-items:center}
.nav a{color:#fff;text-decoration:none;font-size:12px;height:42px;line-height:42px;text-align:center;white-space:nowrap;flex:none;border-right:1px solid #7a7a7a}
.nav a:last-child{border-right:none}
.nav-active{left:258px;top:89px;width:46px;height:7px;border-radius:4px;background:var(--blue)}
.slider{left:94px;top:105px;width:815px;height:306px;background:#fff;box-shadow:0 1px 4px rgba(0,0,0,.25)}
.slide-photo{left:107px;top:116px;width:790px;height:285px;background:linear-gradient(100deg,#8f8f8f,#e8e8e8 45%,#b5b5b5);border:1px solid #555}
.slide-title{left:107px;top:334px;width:790px;text-align:center;font-size:30px;line-height:32px;color:#3c3c3c;text-shadow:0 1px 0 #fff}
.dots{left:120px;top:384px;display:flex;gap:3px}
.dots i{width:10px;height:10px;border-radius:50%;background:#e6e6e6;display:block}
.dots i.on{background:var(--blue)}
.intro{left:104px;top:424px;width:800px;text-align:center;font-size:14.5px;line-height:18px;color:#555}
.card{top:498px;width:200px}
.card .frame{height:100px;border:1px solid #999;padding:5px;background:#fff}
.card .frame div{width:100%;height:100%;background:linear-gradient(135deg,#555,#bdbdbd)}
.card h3{font-weight:400;font-size:13.5px;margin:13px 0 9px;color:#555}
.card p{font-size:10px;line-height:13px;color:var(--muted);text-align:justify}
.more{color:var(--blue);font-size:10px;text-decoration:none}
.rule{height:1px;background:var(--rule)}
.section-title{font-size:13.5px;color:#555}
.feature{left:93px;width:178px}
.toggle{position:absolute;left:0;width:17px;height:17px;border-radius:50%;background:#e9e9e9;border:1px solid #ddd;font-size:13px;line-height:14px;text-align:center;color:#888}
.feature .label{position:absolute;left:33px;font-size:11.5px;color:#777}
.feature .label.open{color:var(--blue)}
.feature-text{position:absolute;left:33px;top:24px;width:165px;font-size:10px;line-height:14.5px;color:var(--muted)}
.project{top:788px;width:166px}
.project .frame{height:99px;border:4px solid #666;background:linear-gradient(135deg,#6d6d6d,#dcdcdc)}
.project h4{font-weight:400;font-size:13.5px;margin:11px 0 6px;color:#555}
.project p{font-size:10px;line-height:14.5px;color:var(--muted);padding-left:2px}
.project .more{padding-left:2px}
.testimonial-photo{left:92px;top:1058px;width:67px;height:63px;border:1px solid #999;padding:4px;background:#fff}
.testimonial-photo div{width:100%;height:100%;background:linear-gradient(135deg,#b08a6e,#e0cbb8)}
.quote{left:170px;top:1060px;width:500px;font-size:10.3px;line-height:16px;color:var(--muted)}
.quote .mark{color:#c8c8c8;font-size:20px;line-height:10px;vertical-align:-6px;font-weight:700}
.author{left:170px;top:1109px;font-size:12px;color:var(--blue)}
.newsletter{left:683px;top:1026px;width:228px;height:112px;border:1px solid #aaa;background:#f4f4f4}
.newsletter h5{position:absolute;left:14px;top:11px;font-weight:400;font-size:13.5px;color:#444}
.newsletter p{position:absolute;left:14px;top:33px;width:205px;font-size:9.6px;line-height:11.5px;color:var(--muted);text-align:justify}
.newsletter .field{position:absolute;left:41px;top:85px;width:113px;height:17px;border:1px solid #777;background:#fff}
.newsletter .btn{position:absolute;left:158px;top:85px;width:57px;height:17px;background:var(--blue);color:#fff;font-size:9.5px;line-height:17px;padding-left:5px}
.newsletter .btn span{position:absolute;right:0;top:0;width:14px;height:17px;background:#3a3a3a}
.newsletter .corner{position:absolute;left:-1px;bottom:-1px}
.footer{left:0;top:1161px;width:1032px;height:39px;background:var(--footer);color:#fff;font-size:10px}
.footer .copy{position:absolute;left:96px;top:15px}
.footer .copy b{font-weight:400;color:#5a8fd8}
.social{position:absolute;top:7px;width:25px;height:25px;border-radius:50%;background:linear-gradient(#eee,#9a9a9a)}
</style>
</head>
<body>
<div class="abs header-band"></div>
<div class="abs feature-band"></div>

<div class="abs brand">
  <div class="brand-mark"></div>
  <div class="brand-name">VANTREL 4<br><span class="brand-sub">MANAGEMENT LIMITED</span></div>
</div>

<div class="abs search">Search
  <svg width="16" height="16" viewBox="0 0 16 16"><circle cx="6.5" cy="6.5" r="5" fill="none" stroke="#999" stroke-width="1.5"/><line x1="10" y1="10" x2="15" y2="15" stroke="#999" stroke-width="2"/></svg>
</div>

<nav class="abs nav">
  <a style="width:74px">Home</a><a style="width:81px">About Us</a><a style="width:104px">Project Control</a><a style="width:148px">Contract Management</a><a style="width:77px">Services</a><a style="width:69px">Project</a><a style="width:107px">Contact Us</a>
</nav>
<div class="abs nav-active"></div>

<div class="abs slider"></div>
<div class="abs slide-photo" role="img" aria-label="Engineers reviewing a technical drawing together"></div>
<div class="abs slide-title">ADVANCED PROJECT<br>MANAGEMENT TECHNIQUES</div>
<div class="abs dots"><i></i><i class="on"></i><i></i></div>

<p class="abs intro">Lorem ipsum dolor sit amet, consectetur adipiscing elit. In ullamcorper, ante non ullamcorper tristique, lorem erat consequat dui, sed ornare enim tortor aliquet dui. Donec libero nisl, consequat sit amet iaculis id, sagittis quis augue.</p>

<div class="abs card" style="left:92px">
  <div class="frame"><div role="img" aria-label="Compass resting on a financial chart"></div></div>
  <h3>Planning &amp; Scheduling</h3>
  <p>Lorem ipsum dolor sit amet, consectetur adipisicing elit. Ut enim ad minim veniam, quis nostrud exercitation.Ullamco laboris nisi ut aliquip ex ea commodo consequat.</p>
  <a class="more">Read More...</a>
</div>
<div class="abs card" style="left:300px">
  <div class="frame"><div role="img" aria-label="Calculator beside banknotes"></div></div>
  <h3>Cost Control</h3>
  <p>Ut enim ad minim veniam, quis nostrud exercitation ullamco. Laboris nisi ut aliquip ex ea commodo consequat.Lorem ipsum dolor sit amet,</p>
  <a class="more">Read More...</a>
</div>
<div class="abs card" style="left:505px">
  <div class="frame"><div role="img" aria-label="Hand rolling dice, risk and quality theme"></div></div>
  <h3>Risk Management</h3>
  <p>Sed do eiusmod tempor incididunt ut labore et dolore magna aliqua. Lorem ipsum dolor sit amet, Ut enim ad minim veniam, quis nostrud exercitation.</p>
  <a class="more">Read More...</a>
</div>
<div class="abs card" style="left:711px">
  <div class="frame"><div role="img" aria-label="Hand stamping a printed report"></div></div>
  <h3>Reporting</h3>
  <p>Sed do eiusmod tempor incididunt ut labore et dolore magna aliqua. Lorem ipsum dolor sit amet, Ut enim ad minim veniam, quis nostrud exercitation.</p>
  <a class="more">Read More...</a>
</div>

<div class="abs rule" style="left:92px;top:725px;width:820px"></div>

<div class="abs section-title" style="left:93px;top:746px">Some Of The Features</div>
<div class="abs feature" style="top:789px;height:190px">
  <span class="toggle" style="top:0">&minus;</span>
  <span class="label open" style="top:2px">Awesome Feature 1</span>
  <p class="feature-text">Sed posuere, mauris in ultricies cursus, augue mi dignissim purus, a laoreet libero leo non neque.</p>
  <div class="rule" style="position:absolute;left:0;top:87px;width:178px"></div>
  <span class="toggle" style="top:102px">+</span>
  <span class="label" style="top:104px">Awesome Feature 2</span>
  <div class="rule" style="position:absolute;left:0;top:135px;width:178px"></div>
  <span class="toggle" style="top:151px">+</span>
  <span class="label" style="top:153px">Awesome Feature 3</span>
  <div class="rule" style="position:absolute;left:0;top:183px;width:178px"></div>
</div>

<div class="abs section-title" style="left:318px;top:746px">Recent Projects</div>
<div class="abs project" style="left:318px">
  <div class="frame" role="img" aria-label="Business handshake by an office window"></div>
  <h4>On the other hand</h4>
  <p>Lorem Ipsum is simply dummy text of the printing and typesetting industry. Lorem Ipsum has been.</p>
  <a class="more">Read More...</a>
</div>
<div class="abs project" style="left:533px">
  <div class="frame" role="img" aria-label="Businessman in an office setting"></div>
  <h4>On the other hand</h4>
  <p>Lorem Ipsum is simply dummy text of the printing and typesetting industry. Lorem Ipsum has been.</p>
  <a class="more">Read More...</a>
</div>
<div class="abs project" style="left:745px">
  <div class="frame" role="img" aria-label="Presenter pointing at a flowchart on a whiteboard"></div>
  <h4>On the other hand</h4>
  <p>Lorem Ipsum is simply dummy text of the printing and typesetting industry. Lorem Ipsum has been.</p>
  <a class="more">Read More...</a>
</div>

<div class="abs rule" style="left:92px;top:1008px;width:820px"></div>

<div class="abs section-title" style="left:93px;top:1024px">Our Testimonials</div>
<div class="abs testimonial-photo"><div role="img" aria-label="Portrait of the client giving the testimonial"></div></div>
<p class="abs quote"><span class="mark">&ldquo;</span> Cras elementum, purus id convallis convallis, dui libero mollis odio, sit amet interdum magna enim nec turpis. Praesent id libero in tortor rhoncus convallis sit amet vel lacus. Phasellus bibendum ultricies nisl et euismod. Aliquam metus neque, fermentum vitae ullamcorper in, fringilla eget ante. <span class="mark">&rdquo;</span></p>
<div class="abs author">Mark Delaney</div>

<div class="abs newsletter">
  <h5>Newsletter Sign Up</h5>
  <p>Sign Up to get notified of new promotions and receive updates about new products and collections.</p>
  <div class="field"></div>
  <div class="btn">Sign Up<span><svg width="14" height="17" viewBox="0 0 14 17"><path d="M5 5 L9 8.5 L5 12Z" fill="#fff"/></svg></span></div>
  <svg class="corner" width="36" height="32" viewBox="0 0 36 32"><path d="M0 0 Q6 22 36 32 L0 32 Z" fill="#fff"/><path d="M0 0 Q6 22 36 32" fill="none" stroke="#aaa"/><path d="M0 0 L0 32 L36 32" fill="none" stroke="#aaa"/></svg>
</div>

<footer class="abs footer">
  <div class="copy">Copyright &copy; 2012 <b>Vantrel 4 Management Limited</b> . All Rights Reserved</div>
  <span class="social" style="left:833px"></span>
  <span class="social" style="left:861px"></span>
  <span class="social" style="left:889px"></span>
</footer>
</body>
</html>
```